Business Cards for Communications Technology Company

We are an innovative software company based in Tropical North Queensland, Australia. We have several brands with a focus on communications software for businesses. We are looking for a business card that is very innovate and creative whilst still remaining professional on a corporate level.

Our internal culture is very progressive and expresses a blend between the clarity of our natural surroundings and the highly technological industry we work in. Our current branding blends a modern minimalist typeface with the desire to push the boundaries in the way we communicate.

This is a corporate level business card for the communications software industry and may possibly also encompass our brands MarNetwork, PelFax, TukMailer and our B2B marketing service—with our companies name being Viresca Partners. Showing other brands on the business card is optional not compulsory.

Technical notes:

-We will attach all logo's and some examples of our corporate branding
- Would be willing to print with various papers, embossed, metallic ink, curved edges etc. in a standard business card size

Sample content:

Rowan Pellick
Senior Account Manager
Phone: 1300 842 916 / +617 4583 2764
Email: r.pellick@viresca.com.au
Web: www.viresca.com.au

Sincerely,
Viresca Partners.

```html
<!DOCTYPE html>
<html lang="en">
<head>
<meta charset="utf-8">
<title>Viresca Partners – Business Card</title>
<link rel="stylesheet" href="https://fonts.googleapis.com/css2?family=Questrial&family=Nunito+Sans:wght@700&display=swap">
<style>
  :root {
    --bg: #ece9e4;
    --black: #0b0b0b;
    --charcoal: #2a2a2a;
    --green: #7fb73a;
    --green-dark: #6a9a35;
    --green-light: #a4cf5a;
    --white: #ffffff;
    --silver: #c9cbcd;
    --text-dark: #3c3c3c;
    --logo-grey: #8f9194;
    --orange: #ee6a22;
    --blue: #3f73b8;
  }
  * { margin: 0; padding: 0; box-sizing: border-box; }
  html, body { width: 900px; height: 1200px; overflow: hidden; }
  body { background: var(--bg); position: relative; font-family: "Questrial", Arial, sans-serif; }

  .card {
    position: absolute;
    border-radius: 26px;
    overflow: hidden;
    box-shadow: 0 6px 14px rgba(0,0,0,.25);
  }
  .card__art { position: absolute; inset: 0; width: 100%; height: 100%; }

  /* Front card */
  .card--front { left: 85px; top: 133px; width: 735px; height: 430px; background: var(--black); }
  .front-logo {
    position: absolute; left: 0; right: 0; top: 140px;
    display: flex; align-items: center; justify-content: center; gap: 16px;
  }
  .logo-dot { width: 58px; height: 58px; border-radius: 50%; background: var(--green); }
  .logo-name { font-size: 54px; letter-spacing: 1px; color: var(--logo-grey); line-height: 1; }
  .brand-row {
    position: absolute; left: 0; right: 0; top: 358px;
    display: flex; justify-content: center; gap: 46px;
    font-family: "Nunito Sans", Arial, sans-serif; font-weight: 700; font-size: 26px;
  }
  .brand { display: flex; align-items: center; gap: 8px; }
  .brand__dot { width: 14px; height: 14px; border-radius: 50%; }
  .brand--net { color: var(--orange); } .brand--net .brand__dot { background: var(--orange); }
  .brand--fax { color: var(--green-dark); } .brand--fax .brand__dot { background: var(--green-dark); }
  .brand--mail { color: var(--blue); } .brand--mail .brand__dot { background: var(--blue); }

  /* Back card */
  .card--back { left: 88px; top: 625px; width: 732px; height: 425px; background: var(--white); }
  .back-logo { position: absolute; left: 60px; top: 70px; display: flex; align-items: center; gap: 14px; }
  .back-logo .logo-dot { width: 64px; height: 64px; }
  .back-logo .logo-name { font-size: 52px; color: #6d6f72; }
  .person { position: absolute; left: 60px; top: 218px; }
  .person__name { font-size: 25px; color: var(--text-dark); letter-spacing: .3px; }
  .person__title { font-size: 18px; color: var(--green-dark); margin-top: 4px; }
  .contact {
    position: absolute; right: 55px; top: 322px;
    list-style: none; color: var(--white); font-size: 15.5px; text-align: right;
  }
  .contact li { display: flex; align-items: center; justify-content: flex-end; gap: 10px; height: 25px; }
  .contact svg { width: 18px; height: 18px; }
</style>
</head>
<body>

<section class="card card--front" aria-label="Card front">
  <svg class="card__art" viewBox="0 0 735 430" preserveAspectRatio="none" aria-hidden="true">
    <defs>
      <radialGradient id="frontGlow" cx="50%" cy="40%" r="60%">
        <stop offset="0" stop-color="#2e2e2e"/>
        <stop offset="1" stop-color="#060606"/>
      </radialGradient>
      <linearGradient id="frontWhite" x1="0" y1="0" x2="1" y2="0">
        <stop offset="0" stop-color="#d9dadb"/>
        <stop offset=".5" stop-color="#ffffff"/>
        <stop offset="1" stop-color="#d4d5d6"/>
      </linearGradient>
    </defs>
    <rect width="735" height="430" fill="url(#frontGlow)"/>
    <path d="M0,335 Q300,290 735,335 V430 H0 Z" fill="var(--green)"/>
    <path d="M0,350 Q320,300 735,350 V430 H0 Z" fill="url(#frontWhite)"/>
  </svg>
  <div class="front-logo">
    <span class="logo-dot"></span>
    <span class="logo-name">Viresca Partners</span>
  </div>
  <div class="brand-row">
    <span class="brand brand--net">MarNetwork<span class="brand__dot"></span></span>
    <span class="brand brand--fax">PelFax<span class="brand__dot"></span></span>
    <span class="brand brand--mail">TukMailer<span class="brand__dot"></span></span>
  </div>
</section>

<section class="card card--back" aria-label="Card back">
  <svg class="card__art" viewBox="0 0 732 425" preserveAspectRatio="none" aria-hidden="true">
    <defs>
      <linearGradient id="backGreen" x1="0" y1="0" x2="1" y2="0">
        <stop offset="0" stop-color="#8cc63f"/>
        <stop offset="1" stop-color="#6f9a3a"/>
      </linearGradient>
      <linearGradient id="swooshGrey" x1="0" y1="0" x2="1" y2="0">
        <stop offset="0" stop-color="#a9abad"/>
        <stop offset=".5" stop-color="#e3e4e5"/>
        <stop offset="1" stop-color="#ffffff"/>
      </linearGradient>
    </defs>
    <path d="M90,318 C260,310 420,230 560,180 C640,152 700,152 732,160 V175 C690,165 630,172 560,200 C420,258 260,325 90,318 Z" fill="var(--green-dark)"/>
    <path d="M0,360 C190,372 340,318 470,255 C580,203 660,178 732,185 V425 H0 Z" fill="url(#backGreen)"/>
    <path d="M0,290 C120,322 280,340 450,300 C300,352 150,362 0,350 Z" fill="url(#swooshGrey)"/>
  </svg>
  <div class="back-logo">
    <span class="logo-dot"></span>
    <span class="logo-name">Viresca Partners</span>
  </div>
  <div class="person">
    <p class="person__name">Rowan Pellick</p>
    <p class="person__title">Senior Account Manager</p>
  </div>
  <ul class="contact">
    <li>1300 842 916 / +617 4583 2764
      <svg viewBox="0 0 18 18"><rect x="1" y="1" width="16" height="16" rx="3" fill="none" stroke="#fff" stroke-width="1.5"/><path d="M4.5,8 Q9,4 13.5,8 V10 H11 V8.5 H7 V10 H4.5 Z M5,11 H13 V14 H5 Z" fill="#fff"/></svg>
    </li>
    <li>r.pellick@viresca.com.au
      <svg viewBox="0 0 18 18"><rect x="1" y="1" width="16" height="16" rx="3" fill="none" stroke="#fff" stroke-width="1.5"/><rect x="4" y="5.5" width="10" height="7" fill="none" stroke="#fff" stroke-width="1.3"/><path d="M4,5.5 L9,9.5 L14,5.5" fill="none" stroke="#fff" stroke-width="1.3"/></svg>
    </li>
    <li>www.viresca.com.au
      <svg viewBox="0 0 18 18"><rect x="1" y="1" width="16" height="16" rx="3" fill="none" stroke="#fff" stroke-width="1.5"/><circle cx="9" cy="9" r="5" fill="none" stroke="#fff" stroke-width="1.2"/><path d="M4,9 H14 M9,4 Q6,9 9,14 M9,4 Q12,9 9,14" fill="none" stroke="#fff" stroke-width="1"/></svg>
    </li>
  </ul>
</section>

</body>
</html>
```